I am a business consultant/coach and I am branding myself 'The Zero Fee Venture Mentor'. My business name is Bright Harbor Advisory.I want an oversized postcard designed for lead generation. It will be sent through the post so will require area for an address and stamp The details that I want on the card are attached plus a photo of myself. Also I have attached a copy of my business card so that you are able to see the style and colors I use. I would like the main headline to be bold red, or bold red background Hope this is enough info.
Target Market(s)
Owners/managers of medium sized businesses
Industry/Entity Type
Business Consultant
Requirements
Must have
- The cards I want to be noticed and professional in appearance, they will be use dfor lead generation and sent through the postal service
Nice to have
- The colors that I use on my business cards are green, grey and white. I want the main headline to be in red or red backgroun dso that it stands out
Should not have
- The words that I have used are basically off my landing page for consistency

```html
<!DOCTYPE html>
<html lang="en">
<head>
<meta charset="utf-8">
<title>Bright Harbor Advisory – Postcard</title>
<link href="https://fonts.googleapis.com/css2?family=Oswald:wght@600;700&family=Open+Sans:wght@400;600;700&family=Montserrat:wght@700&display=swap" rel="stylesheet">
<style>
  :root{
    --red:#e8262a;
    --green:#3cb54a;
    --ink:#1f1f1f;
    --grey-text:#6b6b6b;
    --band-light:#f1f1f1;
    --band-mid:#cfd0d2;
    --band-dark:#bcbdc0;
    --band-pale:#e6e6e7;
    --page:#ececec;
    --white:#ffffff;
    --rule:#9a9a9a;
  }
  *{box-sizing:border-box;margin:0;padding:0}
  html,body{width:937px;height:1200px;overflow:hidden}
  body{background:var(--page);font-family:"Open Sans",Arial,sans-serif;color:var(--ink);position:relative}

  .card{position:absolute;background:var(--white);width:659px;height:511px;box-shadow:0 2px 8px rgba(0,0,0,.18);overflow:hidden}
  .card--front{left:97px;top:61px}
  .card--back{left:177px;top:614px}

  .brand{font-family:"Montserrat",Arial,sans-serif;font-weight:700;color:#4a4a4a;font-size:27px;letter-spacing:-.5px;display:flex;align-items:center;gap:8px}
  .brand__dot{width:12px;height:12px;background:var(--green)}

  /* front */
  .front-header{position:absolute;left:0;top:0;width:100%;height:72px;background:var(--band-light)}
  .front-header .brand{position:absolute;left:17px;top:17px}
  .front-header__contact{position:absolute;right:30px;top:22px;text-align:right;font-size:12.5px;font-weight:600;line-height:17px}

  .headline{position:absolute;left:17px;top:88px;font-family:"Oswald",Impact,sans-serif;font-weight:700;color:var(--red);font-size:39px;line-height:39px;text-transform:uppercase}
  .subhead{position:absolute;left:17px;top:208px;font-weight:700;font-size:18px;letter-spacing:.2px}
  .intro{position:absolute;left:17px;top:241px;width:440px;font-size:15px;line-height:18px;color:var(--grey-text)}
  .intro strong{color:#555}

  .portrait{position:absolute;left:504px;top:124px;width:126px;height:163px;border:2px solid #c8c8c8;background:linear-gradient(180deg,#9fb4c8 0%,#b9a493 55%,#e8e8ea 100%)}

  .promise-band{position:absolute;left:0;top:299px;width:100%;height:79px;background:var(--green);color:var(--white);padding:13px 17px;font-size:15.5px;line-height:25px}
  .promise-band strong{font-weight:700}

  .body-band{position:absolute;left:0;top:383px;width:100%;height:128px;background:var(--band-mid);padding:8px 17px;font-size:12px;line-height:15px;text-align:justify}

  /* back */
  .card--back .brand{position:absolute;left:88px;top:34px;font-size:29px}
  .coach-title{position:absolute;left:0;top:92px;width:339px;height:38px;background:var(--green);color:var(--white);font-size:18px;text-align:center;line-height:38px;text-transform:uppercase}
  .contact-panel{position:absolute;left:0;top:130px;width:339px;height:119px;background:var(--band-dark);text-align:center;font-size:12px;line-height:20px;padding-top:28px}
  .guarantee{position:absolute;left:0;top:249px;width:339px;height:118px;background:var(--band-pale);text-align:center;font-size:11px;line-height:14px;padding-top:12px}
  .guarantee__title{font-weight:700;font-size:13px;margin-bottom:22px}
  .guarantee strong{font-size:12px}
  .cta{position:absolute;left:0;top:367px;width:339px;height:39px;background:var(--green);color:var(--white);font-size:17px;line-height:39px;padding-left:42px}

  .return-address{position:absolute;left:365px;top:22px;font-size:10.5px;line-height:13px;font-weight:600}
  .return-address span{display:block;margin-top:8px}
  .stamp-box{position:absolute;left:553px;top:19px;width:90px;height:61px;border:1px solid #a9a9a9}
  .address-lines{position:absolute;left:382px;top:198px;width:260px}
  .address-lines span{display:block;height:1px;background:var(--rule);margin-bottom:36px}
</style>
</head>
<body>

<section class="card card--front" aria-label="Postcard front">
  <header class="front-header">
    <div class="brand"><span>brightharbor</span><span class="brand__dot"></span></div>
    <div class="front-header__contact">Bright Harbor Advisory<br>brightharbor.com.au</div>
  </header>

  <h1 class="headline">Has your<br>business achieved<br>the outcomes you want?</h1>
  <p class="subhead">It can and I’m prepared to show you how</p>
  <p class="intro">My name is Daniel Whitmore, from Bright Harbor Advisory, the ‘<strong>Zero Fee Venture Mentor</strong>’.</p>

  <div class="portrait" role="img" aria-label="Portrait photo of Daniel Whitmore"></div>

  <div class="promise-band"><strong>If I told you that you can increase your profits, give yourself more time, freedom and peace, what would your answer be...?</strong> Research says you can and quickly</div>

  <div class="body-band">
    <p>Because over 90 percent of small to medium sized business in Australia have a minimum of 12 per cent of their annual turnover tied up in ineffective and inefficient processes?</p>
    <p>The problem is that most business owners focus on their daily challenges unable to free themselves to consider where the ‘hidden profit’ may be locked up within their business.</p>
    <p>I can change this by reviewing your cashflow, systems, staff capability, business culture and Risk. The end result will be more money, time, freedom and peace to live your life that way you desire.</p>
  </div>
</section>

<section class="card card--back" aria-label="Postcard back">
  <div class="brand"><span>brightharbor</span><span class="brand__dot"></span></div>
  <div class="coach-title">Zero Fee Venture Mentor</div>
  <div class="contact-panel">
    If you would like more information go to<br>
    brightharbor.com.au/zerofee or email hello@brightharbor.com.au<br>
    Also you can call me on 0400555218
  </div>
  <div class="guarantee">
    <p class="guarantee__title">MY PROMISE:</p>
    <p>“If I cannot uncover at least 5 times my fee from<br><strong>potential profits hidden within your business</strong><br>after one interview then it is free.”</p>
  </div>
  <div class="cta">visit brightharbor.com.au/zerofee</div>

  <div class="return-address">Bright Harbor Advisory<span>Cedar Bay, NSW<br>Australia</span></div>
  <div class="stamp-box" aria-label="Stamp area"></div>
  <div class="address-lines" aria-label="Address lines"><span></span><span></span><span></span><span></span></div>
</section>

</body>
</html>
```